New Website - vostimo.net

This is what we looking for - http://www.craftlane-example.com/design/583017
Updates

hello, im back and i want some good designs for my website.. i need really creative ideas. this is for a cellphone provider company. Vostimo mobile please provide me a good ideas and i will go with u also to program the website

Font styles to use
Sans Serif

```html
<!DOCTYPE html>
<html lang="en">
<head>
<meta charset="utf-8">
<title>Vostimo mobile</title>
<link href="https://fonts.googleapis.com/css2?family=Open+Sans:wght@400;600;700;800&family=PT+Sans:wght@400;700&family=Oswald:wght@600;700&display=swap" rel="stylesheet">
<style>
:root{
  --blue:#2f6fc0;
  --blue-deep:#1b4f96;
  --blue-light:#4a8fdb;
  --ink:#2b2b2b;
  --muted:#555;
  --paper:#f2f2f2;
  --white:#fff;
  --dark:#1c1c1c;
  --darker:#111;
  --red:#c21d1d;
  --pill:#2e3440;
  --line:#d7d7d7;
}
*{margin:0;padding:0;box-sizing:border-box}
html,body{width:1200px;height:2273px;overflow:hidden}
body{position:relative;font-family:"PT Sans",Arial,sans-serif;color:var(--ink);background:var(--white)}
.abs{position:absolute}

/* top utility bar */
.utility{left:0;top:0;width:1200px;height:82px;background:linear-gradient(#fafafa,#e9e9e9)}
.utility-links{left:86px;top:28px;display:flex;font-family:"Open Sans",sans-serif;font-size:15px;font-weight:600;color:#444}
.utility-links span{padding:0 16px;border-left:1px solid #bbb;line-height:20px}
.utility-links span:first-child{border-left:0;padding-left:0;color:var(--blue)}
.utility-links .quest{color:var(--red);font-weight:700}
.account{left:806px;top:20px;width:150px;height:40px;border:2px solid #999;border-radius:20px;background:linear-gradient(#fff,#ddd);font-family:"Open Sans",sans-serif;font-size:15px;font-weight:600;color:#333;display:flex;align-items:center;justify-content:center;gap:8px}
.search{left:968px;top:20px;width:156px;height:40px;border:2px solid #999;border-radius:20px;background:linear-gradient(#fff,#e4e4e4);font-family:"Open Sans",sans-serif;font-size:14px;color:#888;padding-left:20px;line-height:36px}
.search svg{position:absolute;right:6px;top:5px}
.rule{left:0;top:82px;width:1200px;height:7px;background:var(--blue)}

/* header */
.header{left:0;top:89px;width:1200px;height:75px;background:var(--white)}
.brand{left:80px;top:103px;display:flex;align-items:center;gap:12px}
.brand-dot{width:40px;height:40px;border-radius:50%;background:var(--blue)}
.brand-name{font-family:"Open Sans",sans-serif;font-size:40px;font-weight:600;color:var(--blue);letter-spacing:1px}
.mainnav{left:390px;top:112px;display:flex;font-family:"Open Sans",sans-serif;font-size:14px;color:#333}
.mainnav div{padding:0 14px;border-left:1px solid #999;line-height:17px}
.mainnav div:first-child{border-left:0;padding-left:0;color:var(--blue)}
.mainnav .big{font-size:14px;text-transform:uppercase}
.mainnav .solo{padding-top:17px}
.tag{background:var(--pill);color:var(--white);font-family:"Open Sans",sans-serif;font-size:13px;border-radius:6px;text-align:center;line-height:28px}
.tag-a{left:852px;top:95px;width:330px;height:28px}
.tag-b{left:952px;top:131px;width:230px;height:28px}

/* hero */
.hero{left:0;top:164px;width:1200px;height:461px;background:radial-gradient(ellipse at 70% 40%,#4d94e0 0%,#2462b4 45%,#123b7a 100%);overflow:hidden}
.hero-photo{position:absolute;left:830px;top:0;width:330px;height:461px;background:linear-gradient(180deg,#5a9be0 0%,#3a78c4 60%,#2a5f9e 100%)}
.hero h1{position:absolute;left:75px;top:70px;font-family:"Open Sans",sans-serif;font-weight:800;font-size:42px;line-height:50px;color:var(--white);letter-spacing:-0.5px}
.hero .sub{position:absolute;left:92px;font-family:"Open Sans",sans-serif;font-size:34px;line-height:44px;color:var(--white)}
.hero .sub b{color:#0e2f63;font-weight:700}
.hero .sub em{font-style:normal;color:#7ec2ff;font-weight:700}
.sub-1{top:122px}.sub-2{top:172px}
.signup{position:absolute;left:78px;top:275px;width:536px;height:104px;border-radius:18px;background:linear-gradient(#f4f4f4,#bdbdbd 55%,#8e8e8e);border:3px solid #555;box-shadow:0 6px 14px rgba(0,0,0,.45);font-family:"Oswald",sans-serif;font-weight:700;font-size:58px;color:#333;display:flex;align-items:center;justify-content:center;letter-spacing:1px}

/* welcome */
.welcome{left:0;top:625px;width:1200px;height:386px;background:var(--paper)}
.video{left:68px;top:675px;width:471px;height:261px;border:8px solid #1d6cc4;border-radius:6px;background:#000}
.video .play{position:absolute;left:205px;top:95px;width:55px;height:50px;background:#2a2a2a;border-radius:4px;border:1px solid #555}
.video .bar{position:absolute;left:0;right:0;bottom:0;height:28px;background:#1a1a1a;display:flex;align-items:center;gap:10px;padding:0 12px;font-size:11px;color:#ccc;font-family:Arial,sans-serif}
.video .track{flex:1;height:4px;background:#555}
.welcome h2{position:absolute;left:580px;top:42px;font-family:"Open Sans",sans-serif;font-weight:400;font-size:36px;color:#333}
.welcome p{position:absolute;left:580px;top:114px;width:595px;font-size:14.5px;line-height:24.5px;color:#444;text-align:justify}

/* features */
.features{left:0;top:1011px;width:1200px;height:489px;background:var(--white)}
.col{position:absolute;top:30px;width:232px}
.col h3{font-family:"Open Sans",sans-serif;font-weight:400;font-size:20px;color:#333;text-align:center;padding-bottom:6px;border-bottom:2px solid #8db5e6}
.thumb{height:122px;margin:14px 20px 12px;border-radius:8px}
.t1{background:linear-gradient(135deg,#2b2b2b,#6c9bd2)}
.t2{background:linear-gradient(135deg,#3a3a3a,#8a8a8a)}
.t3{background:linear-gradient(135deg,#2e87d6,#7fb6e8)}
.bul{list-style:none}
.bul li{position:relative;padding-left:38px;font-size:13px;line-height:17px;color:#333;margin-bottom:14px}
.bul li::before{content:"";position:absolute;left:6px;top:2px;width:16px;height:16px;border-radius:50%;border:3px solid var(--blue-deep);border-right-color:transparent}
.c1{left:64px}.c2{left:330px}.c3{left:591px}.c4{left:859px;width:250px}
.c4 .bul{margin-top:18px}
.c4 .bul li{text-align:justify;margin-bottom:16px}
.more{position:absolute;top:421px;width:100px;height:32px;border-radius:16px;background:var(--blue-deep);color:var(--white);font-family:"Open Sans",sans-serif;font-size:13px;text-align:center;line-height:32px}

/* blue band */
.band{left:0;top:1500px;width:1200px;height:387px;background-color:var(--blue);background-image:linear-gradient(rgba(255,255,255,.06) 1px,transparent 1px),linear-gradient(90deg,rgba(255,255,255,.06) 1px,transparent 1px);background-size:22px 22px}
.pane{position:absolute;top:24px;color:var(--white);font-family:"Open Sans",sans-serif}
.pane h4{font-size:29px;font-weight:600;text-align:center;line-height:34px;border-bottom:2px solid rgba(255,255,255,.7);margin:0 auto;width:72%}
.pane .lead{font-size:15px;text-align:center;margin-top:4px;margin-bottom:16px}
.pane ul{list-style:none}
.pane li{font-size:13.5px;padding:10px 0 12px 36px;border-bottom:2px dashed rgba(255,255,255,.55);position:relative}
.pane li::before{content:"";position:absolute;left:4px;top:14px;width:13px;height:8px;background:var(--white);border-radius:6px 0 6px 0}
.pane li:last-child{border-bottom:0}
.wbtn{display:block;margin:10px auto 0;width:190px;height:28px;border-radius:14px;background:var(--white);color:#333;font-size:13px;text-align:center;line-height:28px}
.p1{left:68px;width:332px}.p2{left:477px;width:273px}.p3{left:830px;width:272px}
.tour{display:flex;align-items:center;gap:10px;margin-top:8px;font-size:14px;font-weight:700}
.tour .wbtn{margin:6px 0 0;width:144px}
.tour-img{width:90px;height:62px;border:2px solid #fff;background:linear-gradient(135deg,#c7b08c,#6e5a40)}
.keep{font-size:13px;font-weight:700;letter-spacing:1px;padding-left:36px;margin-top:4px}
.numrow{display:flex;align-items:center;gap:6px;margin:14px 0 0 30px}
.numrow span{width:52px;height:28px;background:var(--white)}
.numrow i{width:10px;height:3px;background:var(--white)}

/* footer */
.footer{left:0;top:1887px;width:1200px;height:329px;background:var(--dark);color:#ddd}
.footer h5{position:absolute;top:50px;font-family:"Open Sans",sans-serif;font-weight:400;font-size:25px;color:var(--white)}
.footer h5::after{content:"";display:block;width:140px;height:3px;background:#444;margin-top:12px}
.fa{left:73px}.fb{left:448px}.fc{left:823px}
.about{position:absolute;left:73px;top:117px;width:300px;font-size:14.5px;line-height:19px;color:var(--white)}
.about p+p{margin-top:19px}
.contact{position:absolute;left:448px;top:117px;font-size:14.5px;line-height:19px;color:#ccc}
.flogo{position:absolute;left:812px;top:109px;width:296px;height:73px;background:#6d6d6d;display:flex;align-items:center;gap:12px;padding-left:22px}
.flogo .brand-dot{background:#2f2f2f}
.flogo .brand-name{color:#2f2f2f;font-size:36px}
.social-tag{position:absolute;left:832px;top:204px;padding:0 8px;height:22px;background:var(--blue);color:var(--white);font-size:12px;line-height:22px;border-radius:3px}
.icons{position:absolute;left:832px;top:237px;display:flex;gap:8px}
.icons span{width:30px;height:30px;border-radius:4px}
.copy{left:0;top:2216px;width:1200px;height:57px;background:var(--darker);color:#ccc;font-size:14px;text-align:center;line-height:57px;border-top:1px solid #333}
</style>
</head>
<body>

<div class="abs utility"></div>
<nav class="abs utility-links"><span>BENIFITS</span><span>EQUIPMENT</span><span>FAQ'S</span><span>FEATURES</span><span>PARTNER</span><span class="quest">REQUEST A QUEST</span></nav>
<div class="abs account"><svg width="14" height="14" viewBox="0 0 14 14"><circle cx="7" cy="4" r="3.2" fill="#333"/><path d="M1 14c0-4 3-6 6-6s6 2 6 6z" fill="#333"/></svg>My Account</div>
<div class="abs search">SEARCH<svg width="28" height="28" viewBox="0 0 28 28"><circle cx="14" cy="14" r="13" fill="#bbb"/><circle cx="12" cy="12" r="5" fill="none" stroke="#555" stroke-width="2"/><path d="M16 16l5 5" stroke="#555" stroke-width="2.5"/></svg></div>
<div class="abs rule"></div>

<header class="abs header"></header>
<div class="abs brand"><span class="brand-dot"></span><span class="brand-name">Vostimo</span></div>
<nav class="abs mainnav">
  <div>In your<br><span class="big">Home</span></div>
  <div>In your<br><span class="big">Office</span></div>
  <div>On your<br><span class="big">Cellphone</span></div>
  <div class="solo big">Support</div>
  <div class="solo big">Contact Us</div>
</nav>
<div class="abs tag tag-a">Business Class Hosted PBX Services</div>
<div class="abs tag tag-b">Data Center Services</div>

<section class="abs hero">
  <div class="hero-photo" role="img" aria-label="Photo of a support agent wearing a headset"></div>
  <h1>A REVOLUTIONARY DIGITAL PHONE</h1>
  <div class="sub sub-1">service that will <em>save you, your family</em>,</div>
  <div class="sub sub-2">and <b>your business</b> lost of money</div>
  <div class="signup">SIGN UP TODAY</div>
</section>

<section class="abs welcome">
  <h2>Welcome to our page</h2>
  <p>Lorem Ipsum is simply dummy text of the printing and typesetting industry. Lorem Ipsum has been the industry's standard dummy text ever since the 1500s, when an unknown printer took a galley of type and scrambled it to make a type specimen book. It has survived not only five centuries, but also the leap into electronic typesetting, remaining essentially unchanged. It was popularised in the 1960s with the release of Typeline sheets containing Lorem Ipsum passages, and more recently with desktop publishing software like Pagecraft Studio including versions of Lorem Ipsum.</p>
</section>
<div class="abs video">
  <div class="play"><svg width="55" height="50" viewBox="0 0 55 50"><path d="M21 15l15 10-15 10z" fill="#fff"/></svg></div>
  <div class="bar"><span>❚❚</span><span>00:00</span><span class="track"></span><span>00:00</span></div>
</div>

<section class="abs features">
  <div class="col c1"><h3>Hosted PBX Benefits</h3><div class="thumb t1" role="img" aria-label="Desk phone beside a tablet"></div>
    <ul class="bul"><li>It has survived not only five centuries, but also the leap into electronic</li><li>Typesetting, remaining essentially unchanged.</li><li>It has survived not only five centuries, but also the leap into electronic</li></ul></div>
  <div class="col c2"><h3>Equipement</h3><div class="thumb t2" role="img" aria-label="Office desk telephone"></div>
    <ul class="bul"><li>It has survived not only five centuries, but also the leap into electronic</li><li>Typesetting, remaining essentially unchanged.</li><li>It has survived not only five centuries, but also the leap into electronic</li></ul></div>
  <div class="col c3"><h3>Advance Voip Services</h3><div class="thumb t3" role="img" aria-label="Globe surrounded by connected devices"></div>
    <ul class="bul"><li>It has survived not only five centuries, but also the leap into electronic</li><li>Typesetting, remaining essentially unchanged.</li><li>It has survived not only five centuries, but also the leap into electronic</li></ul></div>
  <div class="col c4"><h3>Read More</h3>
    <ul class="bul"><li>Lorem Ipsum is simply dummy text of the printing and typesetting industry.</li><li>Lorem Ipsum has been the industry's</li><li>The 1500s, when an unknown printer took a galley of type and scrambled it to make a type specimen book.</li><li>It has survived not only five centuries, but also the leap into electronic</li><li>Typesetting, remaining essentially unchanged.</li></ul></div>
  <div class="more" style="left:176px">Read more</div>
  <div class="more" style="left:447px">Read more</div>
  <div class="more" style="left:719px">Read more</div>
  <div class="more" style="left:994px">Read more</div>
</section>

<section class="abs band">
  <div class="pane p1"><h4>AFFORDABLE</h4><div class="lead">START SAVING TODAY!</div>
    <ul><li>Unlimited local and long distance calling</li><li>5 nation unlimited international</li><li>No set-up, equipment fees, or hidden charges</li><li>No contracts or commitments</li></ul>
    <span class="wbtn">Compare rates &amp; plans</span></div>
  <div class="pane p2"><h4>POWERFUL</h4><div class="lead">INCREDIBLE FEATURES, STANDARD</div>
    <ul><li>Seamless integration with Mailbridge</li><li>Get calls and voicemail anywhere</li><li>100% hurricane proof</li><li><b>Featuring the power of Linkvora!</b></li></ul>
    <div class="tour"><div>See Vostimo in action<span class="wbtn">Take the tour</span></div><div class="tour-img" role="img" aria-label="Office workspace preview"></div></div></div>
  <div class="pane p3"><h4>FLEXIBLE</h4><div class="lead">SERVICE ON YOUR OWN TERMS</div>
    <div class="keep">KEEP YOUR NUMBER!</div>
    <div class="numrow"><span></span><i></i><span></span><i></i><span></span></div>
    <span class="wbtn" style="width:140px">Check Availibility</span>
    <ul style="margin-top:8px"><li>Choose your own area code</li><li>Custo-tailored business solution, both hosted and local</li></ul>
    <span class="wbtn" style="width:150px">Learn how it works</span></div>
</section>

<footer class="abs footer">
  <h5 class="fa">About us</h5><h5 class="fb">Contact us</h5><h5 class="fc">follow us</h5>
  <div class="about"><p>Lorem ipsum dolor sit amet, consectetur adipisicing elit, sed do eiusmod tempor incididunt. Estibulum non aliquam odio, vitae vehicula dolor.</p><p>Sed congue ligula nisi, id tempor nibh tempor molestie. Duis interdum neque ligula, sit amet porttitor odio</p></div>
  <div class="contact">Your Company<br>121th Street North East<br>Brookfield, NV 80412<br><br>Phone : 000)-123-4578<br>Fax : (000)-123-4578<br>E-mail : hello@vostimo.net</div>
  <div class="flogo"><span class="brand-dot"></span><span class="brand-name">Vostimo</span></div>
  <div class="social-tag">Social</div>
  <div class="icons"><span style="background:#3b5a9a"></span><span style="background:#3aa6e0"></span><span style="background:#d9463a"></span><span style="background:#d3273c"></span><span style="background:#e0417f"></span><span style="background:#4a5a74"></span></div>
</footer>
<div class="abs copy">Copyright © 2014 vostimo</div>

</body>
</html>
```